Plastic Jar Catalogue 7

We are a plastic factory manufacturing different size of plastic jars, which mostly use for spice and grinded coffee. I need the catalogue to be 3 pages:First page: an attractive cover shows the factory's name and logo with a space for products’ picture. Second page: is an items page which I prefer to be enough for 4 items with a space for item number and description under each item. Last page: to be for factory’s address and contact details.

```html
<!DOCTYPE html>
<html lang="en">
<head>
<meta charset="utf-8">
<title>Clearvale Plastic Works – Catalogue</title>
<link rel="stylesheet" href="https://fonts.googleapis.com/css2?family=Bebas+Neue&family=Source+Sans+3:wght@400;600;700&display=swap">
<style>
  :root {
    --backdrop: #6f6e73;
    --teal: #1f97b1;
    --green: #8bc34a;
    --white: #ffffff;
    --ink: #111111;
    --brand-ink: #222222;
    --jar-light: #eef0f1;
    --jar-dark: #b9bec2;
  }
  html, body { margin: 0; padding: 0; overflow: hidden; }
  body {
    width: 1200px; height: 960px;
    background: var(--backdrop);
    position: relative;
    font-family: "Source Sans 3", sans-serif;
  }
  .page {
    position: absolute;
    width: 469px; height: 663px;
    background: var(--white);
    transform: scale(0.8);
    transform-origin: 0 0;
    overflow: hidden;
  }
  .page--cover { left: 17.6px; top: 212px; }
  .page--items { left: 410.4px; top: 217.6px; }
  .page--back  { left: 807.2px; top: 216.8px; }
  .page__art { position: absolute; inset: 0; width: 469px; height: 663px; }
  .page__footer-band {
    position: absolute; left: 0; right: 0; bottom: 0; height: 12px;
    background: var(--teal);
  }

  /* Cover */
  .cover-brand {
    position: absolute; left: 0; right: 0; top: 418px;
    text-align: center; color: var(--brand-ink);
    font-weight: 400; letter-spacing: 3px; font-size: 20px; line-height: 27px;
    text-transform: uppercase;
  }
  .cover-brand__dot {
    display: block; width: 46px; height: 46px; border-radius: 50%;
    background: var(--teal); margin: 0 auto 12px;
  }
  .cover-title {
    position: absolute; left: 0; right: 0; top: 560px;
    text-align: center; margin: 0; white-space: nowrap;
    font-family: "Bebas Neue", sans-serif; font-weight: 400;
    font-size: 46px; line-height: 1; color: var(--teal);
    letter-spacing: 0.3px;
  }

  /* Product frames */
  .product-frame {
    position: absolute; box-sizing: border-box;
    border: 5px solid var(--teal); border-radius: 50%;
    background: var(--white);
    display: flex; align-items: center; justify-content: center;
  }
  .product-frame--on-teal { border-color: var(--white); }
  .product-frame__photo {
    width: 62%; height: 66%; border-radius: 10px;
    background: linear-gradient(180deg, var(--jar-dark) 0%, var(--jar-dark) 22%, var(--jar-light) 26%, #dfe3e5 100%);
  }

  /* Item entries */
  .item { position: absolute; width: 285px; }
  .item__title {
    margin: 0 0 8px; color: var(--teal);
    font-weight: 700; font-size: 18px; line-height: 1;
  }
  .item__text {
    margin: 0; color: var(--ink); font-weight: 600;
    font-size: 9.2px; line-height: 11.2px; text-align: justify;
  }

  /* Back page */
  .back-brand {
    position: absolute; left: 30px; top: 560px;
    color: var(--white); font-weight: 600;
    font-size: 11px; line-height: 14px; letter-spacing: 1.6px;
    text-transform: uppercase; text-align: center;
  }
  .back-brand__dot {
    display: block; width: 30px; height: 30px; border-radius: 50%;
    background: var(--white); margin: 0 auto 8px;
  }
  .contact {
    position: absolute; left: 210px; top: 596px; width: 240px;
    margin: 0; color: var(--white); font-style: normal;
    font-size: 11px; line-height: 14px;
  }
  .contact__label { font-weight: 700; }
</style>
</head>
<body>

<!-- Cover -->
<section class="page page--cover">
  <svg class="page__art" viewBox="0 0 469 663" aria-hidden="true">
    <rect width="469" height="663" fill="var(--teal)"/>
    <path d="M0,445 C70,350 170,325 280,355 C370,380 430,370 469,320 L469,663 L0,663 Z" fill="var(--white)"/>
    <path d="M0,205 C130,185 260,225 345,300 C385,335 420,356 469,340 L469,322 C430,340 400,335 360,310 C270,250 140,235 0,262 Z" fill="var(--white)"/>
    <path d="M0,213 C125,196 255,232 340,302 C378,334 410,352 440,354 C405,348 375,333 340,312 C250,258 125,240 0,255 Z" fill="var(--green)"/>
  </svg>
  <div class="product-frame product-frame--on-teal" style="left:170px; top:36px; width:130px; height:130px;">
    <div class="product-frame__photo" role="img" aria-label="Space for a product photo of clear plastic jars"></div>
  </div>
  <div class="cover-brand">
    <span class="cover-brand__dot"></span>
    Clearvale Plastic<br>Works
  </div>
  <h1 class="cover-title">CLEARVALE PLASTIC WORKS</h1>
  <div class="page__footer-band"></div>
</section>

<!-- Items -->
<section class="page page--items">
  <div class="product-frame" style="left:23px; top:64px; width:127px; height:127px;">
    <div class="product-frame__photo" role="img" aria-label="Photo of a clear plastic jar with a silver screw lid"></div>
  </div>
  <article class="item" style="left:160px; top:65px;">
    <h2 class="item__title">Title Lorem Ipsum</h2>
    <p class="item__text">"Lorem ipsum dolor sit amet, consectetur adipiscing elit, sed do eiusmod tempor incididunt ut labore et dolore magna aliqua. Ut enim ad minim veniam, quis nostrud exercitation ullamco laboris nisi ut aliquip ex ea commodo consequat. Duis aute irure dolor in reprehenderit in voluptate velit esse cillum dolore eu fugiat nulla pariatur. Excepteur sint occaecat cupidatat non proident, sunt in culpa qui officia deserunt mollit anim id est laborum."</p>
  </article>

  <article class="item" style="left:22px; top:206px;">
    <h2 class="item__title">Title Lorem Ipsum</h2>
    <p class="item__text">"Lorem ipsum dolor sit amet, consectetur adipiscing elit, sed do eiusmod tempor incididunt ut labore et dolore magna aliqua. Ut enim ad minim veniam, quis nostrud exercitation ullamco laboris nisi ut aliquip ex ea commodo consequat. Duis aute irure dolor in reprehenderit in voluptate velit esse cillum dolore eu fugiat nulla pariatur. Excepteur sint occaecat cupidatat non proident, sunt in culpa qui officia deserunt mollit anim id est laborum."</p>
  </article>
  <div class="product-frame" style="left:319px; top:196px; width:127px; height:127px;">
    <div class="product-frame__photo" role="img" aria-label="Photo of a clear plastic jar with a silver screw lid"></div>
  </div>

  <div class="product-frame" style="left:23px; top:339px; width:127px; height:127px;">
    <div class="product-frame__photo" role="img" aria-label="Photo of a clear plastic jar with a silver screw lid"></div>
  </div>
  <article class="item" style="left:160px; top:347px;">
    <h2 class="item__title">Title Lorem Ipsum</h2>
    <p class="item__text">"Lorem ipsum dolor sit amet, consectetur adipiscing elit, sed do eiusmod tempor incididunt ut labore et dolore magna aliqua. Ut enim ad minim veniam, quis nostrud exercitation ullamco laboris nisi ut aliquip ex ea commodo consequat. Duis aute irure dolor in reprehenderit in voluptate velit esse cillum dolore eu fugiat nulla pariatur. Excepteur sint occaecat cupidatat non proident, sunt in culpa qui officia deserunt mollit anim id est laborum."</p>
  </article>

  <article class="item" style="left:22px; top:488px;">
    <h2 class="item__title">Title Lorem Ipsum</h2>
    <p class="item__text">"Lorem ipsum dolor sit amet, consectetur adipiscing elit, sed do eiusmod tempor incididunt ut labore et dolore magna aliqua. Ut enim ad minim veniam, quis nostrud exercitation ullamco laboris nisi ut aliquip ex ea commodo consequat. Duis aute irure dolor in reprehenderit in voluptate velit esse cillum dolore eu fugiat nulla pariatur. Excepteur sint occaecat cupidatat non proident, sunt in culpa qui officia deserunt mollit anim id est laborum."</p>
  </article>
  <div class="product-frame" style="left:319px; top:472px; width:127px; height:127px;">
    <div class="product-frame__photo" role="img" aria-label="Photo of a clear plastic jar with a silver screw lid"></div>
  </div>
  <div class="page__footer-band"></div>
</section>

<!-- Back -->
<section class="page page--back">
  <svg class="page__art" viewBox="0 0 469 663" aria-hidden="true">
    <path d="M0,432 C60,388 150,385 250,410 C350,436 425,402 469,344 L469,663 L0,663 Z" fill="var(--teal)"/>
    <path d="M0,452 C40,420 90,418 140,440 C210,470 260,530 340,548 C400,560 440,550 469,540 L469,583 C420,590 370,588 320,575 C230,550 160,470 100,450 C60,438 30,440 0,462 Z" fill="var(--white)"/>
    <path d="M40,432 C110,430 180,490 240,520 C300,548 380,552 469,532 L469,572 C390,585 320,576 260,548 C180,510 110,445 40,432 Z" fill="var(--green)"/>
  </svg>
  <div class="product-frame" style="left:37px; top:68px; width:145px; height:145px;">
    <div class="product-frame__photo" role="img" aria-label="Photo of a clear plastic jar with a silver screw lid"></div>
  </div>
  <div class="product-frame" style="left:203px; top:68px; width:145px; height:145px;">
    <div class="product-frame__photo" role="img" aria-label="Photo of a clear plastic jar with a silver screw lid"></div>
  </div>
  <div class="product-frame" style="left:124px; top:207px; width:145px; height:145px;">
    <div class="product-frame__photo" role="img" aria-label="Photo of a clear plastic jar with a silver screw lid"></div>
  </div>
  <div class="product-frame" style="left:290px; top:207px; width:145px; height:145px;">
    <div class="product-frame__photo" role="img" aria-label="Photo of a clear plastic jar with a silver screw lid"></div>
  </div>
  <div class="back-brand">
    <span class="back-brand__dot"></span>
    Clearvale Plastic<br>Works
  </div>
  <address class="contact">
    <span class="contact__label">Address:</span> 14 Mill Road, Harborfield Industrial Park<br>
    <span class="contact__label">Phone:</span> +00 123 456 7890<br>
    <span class="contact__label">Email:</span> sales@clearvale-example.com
  </address>
</section>

</body>
</html>
```